Online-Marketing Material für Immobilienmakler
Zielgruppe
Ich bin Immobilienmakler und beschäftige mich mit der Vermietung / Verkauf von Immobilien. Zielgruppe sind Käufer / Verkäufer bzw. Vermieter und Mieter
Aufgabenstellung
Das Design soll sich am bestehenden CI orientieren, gleichzeitig modern gestaltet werden. Hierbei geht es mir um die Erstellung von Desginvorlagen für Post in Social-Media-Kanälen, welche ich je nach Inhalt entsprechend anpassen kann.
Inbesondere soll es eine Vorlage für die Vorstellung von neuen Objekten geben, welche immer wieder genutzt werden kann und daher die Inhalte in Canva anpassbar sind.

```html
<!DOCTYPE html>
<html lang="de">
<head>
<meta charset="utf-8">
<title>Objektvorstellung – Lindenhof Immobilien</title>
<link rel="stylesheet" href="https://fonts.googleapis.com/css2?family=Red+Hat+Display:wght@400;500;600;700&display=swap">
<style>
:root{
  --green:#82bc41;
  --green-dark:#6ca335;
  --blue:#0784c3;
  --white:#ffffff;
  --text-font:"Red Hat Display",sans-serif;
}
*{margin:0;padding:0;box-sizing:border-box}
html,body{width:1200px;height:1117px;overflow:hidden;background:#fff}
.post{position:relative;width:1200px;height:1117px;overflow:hidden;font-family:var(--text-font);background:var(--white)}
.hero-photo{position:absolute;left:0;top:0;width:1200px;height:435px;
  background:linear-gradient(180deg,#7f97ae 0%,#b9b4b4 32%,#d8ccc6 48%,#6b6a6a 62%,#2e3a2a 82%,#3b3329 100%)}
.brand-halo{position:absolute;left:296px;top:0;width:607px;height:203px;border-radius:0 0 46px 46px;background:rgba(255,255,255,.35)}
.brand-box{position:absolute;left:314px;top:0;width:571px;height:185px;border-radius:0 0 38px 38px;background:var(--white);
  display:flex;align-items:center;justify-content:center;gap:16px}
.brand-mark{width:40px;height:40px;background:var(--green);flex:none}
.brand-name{font-weight:700;font-size:44px;color:var(--blue);letter-spacing:-.5px;white-space:nowrap}
.feature-panel{position:absolute;left:0;top:435px;width:650px;height:546px;background:var(--green);border-radius:0 44px 44px 0;z-index:2}
.feature{position:absolute;left:84px;display:flex;align-items:center}
.feature-icon{width:66px;height:66px;border:8px solid var(--white);border-radius:50%;flex:none}
.feature-text{position:absolute;left:126px;width:362px;color:var(--white);font-size:27px;line-height:30px;font-weight:400;letter-spacing:-.2px}
.feature-rule{position:absolute;left:63px;width:528px;height:4px;background:var(--green-dark)}
.offer-area{position:absolute;left:600px;top:435px;width:600px;height:361px;background:var(--blue)}
.headline{position:absolute;left:650px;top:470px;width:550px;text-align:center;color:var(--white);font-weight:700;font-size:33px;line-height:41px;letter-spacing:-.3px}
.object-frame{position:absolute;left:736px;top:606px;width:372px;height:372px;border-radius:50%;background:var(--white);
  box-shadow:0 18px 22px -12px rgba(0,0,0,.35)}
.object-ring{position:absolute;left:12px;top:12px;width:348px;height:348px;border-radius:50%;background:var(--green)}
.object-photo{position:absolute;left:14px;top:14px;width:320px;height:320px;border-radius:50%;
  background:linear-gradient(180deg,#a9c3dd 0%,#dfe7ee 25%,#4f6a3b 40%,#b85c42 52%,#f2f2f0 68%,#9a9a96 100%)}
.contact-bar{position:absolute;left:0;top:1002px;width:1200px;height:115px}
.contact-bar .bar-shapes{position:absolute;left:0;top:0}
.phone{position:absolute;left:76px;top:29px;display:flex;align-items:center;gap:16px;color:var(--white);font-weight:600;font-size:43px;letter-spacing:-.3px}
.phone-icon{width:50px;height:50px;border-radius:50%;background:var(--white);display:flex;align-items:center;justify-content:center;flex:none}
.online{position:absolute;left:625px;top:40px;display:flex;align-items:center;color:var(--white);font-size:20px;font-weight:500}
.online svg{margin-right:12px;flex:none}
.online-divider{width:2px;height:26px;background:rgba(255,255,255,.45);margin:0 16px}
</style>
</head>
<body>
<main class="post">
  <div class="hero-photo" role="img" aria-label="Foto eines modernen Einfamilienhauses mit Solardach in der Abenddämmerung vor Bäumen"></div>

  <div class="brand-halo"></div>
  <header class="brand-box">
    <span class="brand-mark"></span>
    <span class="brand-name">Lindenhof Immobilien</span>
  </header>

  <div class="offer-area"></div>
  <h1 class="headline">Das “Hier Kann Ich Schnell<br>Einziehen” Haus In Toller<br>Lage Von Wendach</h1>

  <section class="feature-panel">
    <div class="feature" style="top:62px"><span class="feature-icon"></span><p class="feature-text" style="top:-22px">Lorem ipsum dolor sit amet, consectetuer adipiscing elit, sed nonummy nibh.</p></div>
    <div class="feature-rule" style="top:185px"></div>
    <div class="feature" style="top:230px"><span class="feature-icon"></span><p class="feature-text" style="top:-22px">Lorem ipsum dolor sit amet, consectetuer adipiscing elit, sed nonummy nibh.</p></div>
    <div class="feature-rule" style="top:357px"></div>
    <div class="feature" style="top:398px"><span class="feature-icon"></span><p class="feature-text" style="top:-22px">Lorem ipsum dolor sit amet, consectetuer adipiscing elit, sed nonummy nibh.</p></div>
  </section>

  <div class="object-frame">
    <div class="object-ring">
      <div class="object-photo" role="img" aria-label="Foto des angebotenen weißen Hauses mit rotem Ziegeldach, Carport und Bergen im Hintergrund"></div>
    </div>
  </div>

  <footer class="contact-bar">
    <svg class="bar-shapes" width="1200" height="115" viewBox="0 0 1200 115">
      <rect x="0" y="14" width="1200" height="101" style="fill:#82bc41"/>
      <path d="M0 0 H544 Q570 0 584 22 L644 115 H0 Z" style="fill:#0784c3"/>
    </svg>
    <div class="phone">
      <span class="phone-icon">
        <svg width="28" height="28" viewBox="0 0 24 24"><path style="fill:#0784c3" d="M6.62 10.79a15.05 15.05 0 0 0 6.59 6.59l2.2-2.2a1 1 0 0 1 1.01-.24c1.12.37 2.33.57 3.58.57a1 1 0 0 1 1 1V20a1 1 0 0 1-1 1A17 17 0 0 1 3 4a1 1 0 0 1 1-1h3.5a1 1 0 0 1 1 1c0 1.25.2 2.45.57 3.57a1 1 0 0 1-.25 1.02l-2.2 2.2z"/></svg>
      </span>
      0 7345 / 216 4490
    </div>
    <div class="online">
      <svg width="26" height="18" viewBox="0 0 26 18"><rect x="1" y="1" width="24" height="16" fill="none" stroke="#fff" stroke-width="2"/><path d="M1 1 L13 10 L25 1 M1 17 L10 8 M25 17 L16 8" fill="none" stroke="#fff" stroke-width="2"/></svg>
      info@lindenhof-immo.de
      <span class="online-divider"></span>
      <svg width="22" height="22" viewBox="0 0 22 22"><g fill="none" stroke="#fff" stroke-width="1.8"><circle cx="11" cy="11" r="9.5"/><ellipse cx="11" cy="11" rx="4.5" ry="9.5"/><path d="M1.5 11h19M3 6h16M3 16h16"/></g></svg>
      www.lindenhof-immo.de
    </div>
  </footer>
</main>
</body>
</html>
```